M25 Billboard Advert Required Please

I need an advert for a motorway Billboard on the M25 , the advert should show the following in big letters:
GUTTER CLEANING
DALRYNFLUES.COM and a small logo off to the side (Our logo is attached)

The printer has requested the following (Important please) the advert has to be
pdf file / 300 dpi/landscape orientation / scaled to a minimum 25% advert size ( this particular site is 22ft x 10ft so 25% of this please). Please also make sure that the artwork is embedded and outlined correctly if this is incorrect it will affect the printing of the banner.

Target Market(s)

General Public

Industry/Entity Type

Gutter Cleaning

Requirements
Should not have
• No Change to our Logo

```html
<!DOCTYPE html>
<html lang="en">
<head>
<meta charset="utf-8">
<title>Gutter Cleaning Billboard</title>
<link rel="stylesheet" href="https://fonts.googleapis.com/css2?family=Anton&family=Montserrat:wght@500;600;700;800;900&display=swap">
<style>
  :root {
    --red: #f50009;
    --red-deep: #c4000a;
    --black: #1b1b1b;
    --white: #ffffff;
    --paper: #f4f4f4;
    --ink: #111111;
    --stage-dark: #6f6f6f;
    --stage-light: #ececec;
  }
  * { margin: 0; padding: 0; box-sizing: border-box; }
  html, body { width: 976px; height: 1200px; overflow: hidden; }
  body {
    background: linear-gradient(135deg, var(--stage-dark) 0%, #9a9a9a 50%, var(--stage-light) 100%);
    position: relative;
    font-family: "Montserrat", Arial, sans-serif;
  }
  .billboard {
    position: absolute;
    left: 38px; top: 395px;
    width: 900px; height: 409px;
    background: linear-gradient(90deg, var(--white) 0%, var(--paper) 100%);
    box-shadow: -6px 8px 14px rgba(0,0,0,0.45);
    overflow: hidden;
  }
  .headline { position: absolute; left: 0; top: 0; overflow: visible; }
  .headline text { font-family: "Anton", "Impact", sans-serif; }
  .headline .word-gutter { fill: var(--red); filter: drop-shadow(4px 4px 0 rgba(0,0,0,0.13)); }
  .headline .word-cleaning { fill: var(--white); filter: drop-shadow(4px 4px 0 rgba(0,0,0,0.35)); }

  .band-dark {
    position: absolute; left: 0; top: 166px;
    width: 900px; height: 152px;
    background: linear-gradient(90deg, #2a2a2a 0%, var(--black) 60%, #000 100%);
  }

  .service {
    position: absolute; left: 592px;
    display: flex; align-items: center;
  }
  .service-icon { width: 42px; height: 40px; }
  .service-bar { width: 3px; height: 40px; background: var(--ink); margin: 0 8px 0 4px; }
  .service-text { line-height: 1; }
  .service-kind { color: var(--red); font-weight: 900; font-size: 20px; letter-spacing: 0.2px; display: block; }
  .service-name { color: var(--ink); font-weight: 500; font-size: 20px; letter-spacing: 0.6px; display: block; margin-top: 7px; }
  .service.residential { top: 26px; }
  .service.commercial { top: 96px; }
  .service-divider { position: absolute; left: 590px; top: 85px; width: 273px; height: 2px; background: var(--ink); }

  .experience { position: absolute; left: 611px; top: 0; width: 253px; height: 152px; color: var(--white); }
  .exp-over { position: absolute; top: 22px; left: 0; font-weight: 800; font-size: 19px; display: flex; align-items: center; width: 253px; }
  .exp-over::after { content: ""; flex: 1; height: 1px; background: #cfcfcf; margin-left: 6px; }
  .exp-years { position: absolute; top: 43px; left: -2px; font-weight: 900; font-size: 50px; color: var(--red); letter-spacing: -0.5px; line-height: 1; white-space: nowrap; }
  .exp-note { position: absolute; top: 95px; left: 0; font-weight: 800; font-size: 14.5px; letter-spacing: 0.3px; white-space: nowrap; }
  .exp-rule { position: absolute; top: 125px; left: 1px; width: 247px; height: 1px; background: #cfcfcf; }

  .quote { position: absolute; left: 38px; top: 318px; }
  .quote-label { position: absolute; left: 5px; top: 10px; font-weight: 800; font-size: 20px; color: var(--ink); white-space: nowrap; }
  .quote-label em { font-style: normal; color: var(--red); }
  .quote-phone { position: absolute; left: 0; top: 40px; display: flex; align-items: center; white-space: nowrap; }
  .quote-phone svg { width: 29px; height: 29px; margin-right: 8px; }
  .quote-phone span { font-weight: 800; font-size: 35px; color: var(--ink); letter-spacing: 0.3px; }

  .contact-strip {
    position: absolute; left: 370px; top: 338px;
    width: 540px; height: 49px;
    background: linear-gradient(90deg, var(--red) 0%, var(--red-deep) 100%);
    clip-path: polygon(23px 0, 100% 0, 100% 100%, 0 100%);
    display: flex; align-items: center;
    padding-left: 23px;
    color: var(--white); font-size: 18.5px; font-weight: 500; white-space: nowrap;
  }
  .contact-strip b { font-weight: 800; }
  .contact-strip svg { width: 13px; height: 13px; margin-right: 6px; }
  .contact-strip .sep { margin: 0 6px; }
</style>
</head>
<body>
  <main class="billboard" aria-label="Gutter cleaning billboard">
    <div class="band-dark">
      <div class="experience">
        <div class="exp-over">OVER</div>
        <div class="exp-years">10 YEARS</div>
        <div class="exp-note">OF INDUSTRY EXPERIENCE</div>
        <div class="exp-rule"></div>
      </div>
    </div>

    <svg class="headline" width="600" height="318" viewBox="0 0 600 318">
      <text class="word-gutter" x="37" y="145" font-size="130" textLength="408" lengthAdjust="spacingAndGlyphs">GUTTER</text>
      <text class="word-cleaning" x="37" y="298" font-size="130" textLength="520" lengthAdjust="spacingAndGlyphs">CLEANING</text>
    </svg>

    <div class="service residential">
      <svg class="service-icon" viewBox="0 0 42 40" aria-hidden="true">
        <g fill="#f50009">
          <rect x="2" y="4" width="20" height="34"/>
          <rect x="0" y="2" width="24" height="4"/>
        </g>
        <g fill="#fff">
          <rect x="5" y="9" width="4" height="4"/><rect x="12" y="9" width="4" height="4"/>
          <rect x="5" y="17" width="4" height="4"/><rect x="12" y="17" width="4" height="4"/>
          <rect x="5" y="25" width="4" height="4"/>
        </g>
        <path d="M16 26 L29 14 L42 26 L39 26 L39 38 L19 38 L19 26 Z" fill="#fff"/>
        <path d="M18 26 L29 16 L40 26 L37 26 L37 37 L21 37 L21 26 Z" fill="#f50009"/>
        <rect x="26" y="29" width="6" height="8" fill="#fff"/>
      </svg>
      <div class="service-bar"></div>
      <div class="service-text">
        <span class="service-kind">RESIDENTIAL</span>
        <span class="service-name">GUTTER CLEANING</span>
      </div>
    </div>
    <div class="service-divider"></div>
    <div class="service commercial">
      <svg class="service-icon" viewBox="0 0 42 40" aria-hidden="true">
        <g fill="#f50009">
          <rect x="6" y="4" width="14" height="34"/>
          <rect x="20" y="14" width="16" height="24"/>
          <rect x="10" y="0" width="3" height="5"/>
          <rect x="3" y="37" width="36" height="3"/>
        </g>
        <g fill="#fff">
          <rect x="9" y="10" width="3" height="3"/><rect x="14" y="10" width="3" height="3"/>
          <rect x="9" y="17" width="3" height="3"/><rect x="14" y="17" width="3" height="3"/>
          <rect x="9" y="24" width="3" height="3"/><rect x="14" y="24" width="3" height="3"/>
          <rect x="24" y="19" width="3" height="3"/><rect x="30" y="19" width="3" height="3"/>
          <rect x="24" y="26" width="3" height="3"/><rect x="30" y="26" width="3" height="3"/>
        </g>
      </svg>
      <div class="service-bar"></div>
      <div class="service-text">
        <span class="service-kind">COMMERCIAL</span>
        <span class="service-name">GUTTER CLEANING</span>
      </div>
    </div>

    <div class="quote">
      <div class="quote-label">REQUEST <em>A FREE QUOTE:</em></div>
      <div class="quote-phone">
        <svg viewBox="0 0 30 30" aria-hidden="true">
          <circle cx="15" cy="15" r="15" fill="#f50009"/>
          <path d="M9 8 C8 9 7 11 8 13 C10 18 13 21 18 23 C20 24 22 23 23 21 L20 18 L17.5 19.5 C15 18 12.5 15.5 11 13 L12.5 10.5 Z" fill="#fff"/>
        </svg>
        <span>0800 047 3391</span>
      </div>
    </div>

    <div class="contact-strip">
      <svg viewBox="0 0 14 14" aria-hidden="true">
        <circle cx="7" cy="7" r="7" fill="#fff"/>
        <g fill="none" stroke="#c4000a" stroke-width="1">
          <circle cx="7" cy="7" r="5"/><ellipse cx="7" cy="7" rx="2.2" ry="5"/><line x1="2" y1="7" x2="12" y2="7"/>
        </g>
      </svg>
      <span>www.<b>dalrynflues</b>.com</span>
      <span class="sep">|</span>
      <svg viewBox="0 0 14 14" aria-hidden="true">
        <circle cx="7" cy="7" r="7" fill="#fff"/>
        <rect x="3.5" y="4.5" width="7" height="5" fill="none" stroke="#c4000a" stroke-width="1"/>
        <polyline points="3.5,4.5 7,7.5 10.5,4.5" fill="none" stroke="#c4000a" stroke-width="1"/>
      </svg>
      <span>info@<b>dalrynflues</b>.com</span>
    </div>
  </main>
</body>
</html>
```